Business Card Design Project

Brenton
Sales Manager

38750 Harlow Ave, Suite 415
Irvine, CA 92604

Tel: 714-382-5061
Fax: 877-524-3917
E-mail: brenton@lumobravo.com

Target Market(s)

We are the distributor and wholesaler, the business card design want to show we are a strong company.

Industry/Entity Type

Business

Colors

Designer to choose colors to be used in the design.

```html
<!DOCTYPE html>
<html lang="en">
<head>
<meta charset="utf-8">
<title>Lumo Bravo – Business Card</title>
<link rel="stylesheet" href="https://fonts.googleapis.com/css2?family=Oswald:wght@500;600&family=Raleway:wght@500;600;700&display=swap">
<style>
  :root {
    --backdrop: #e9ebe6;
    --paper: #ffffff;
    --leaf: #8cbb4c;
    --leaf-deep: #3f7a2e;
    --ink-light: #ffffff;
    --icon-accent: #d8332b;
  }
  * { box-sizing: border-box; margin: 0; padding: 0; }
  html, body {
    width: 1200px; height: 816px; overflow: hidden;
    background: var(--backdrop);
  }
  .card {
    position: absolute; left: 100px; top: 118px;
    width: 1000px; height: 580px;
    border-radius: 44px; overflow: hidden;
    background: var(--paper);
    box-shadow: 0 10px 30px rgba(0,0,0,0.12);
  }
  .brand-side {
    position: absolute; left: 0; top: 0; width: 440px; height: 100%;
    display: flex; align-items: center; justify-content: center; gap: 14px;
  }
  .brand-dot {
    width: 22px; height: 22px; border-radius: 50%; background: var(--leaf);
  }
  .brand-name {
    font-family: "Raleway", sans-serif; font-weight: 700;
    font-size: 50px; color: var(--leaf-deep); letter-spacing: 1px;
  }
  .info-panel {
    position: absolute; left: 440px; top: 0; width: 560px; height: 100%;
    background: var(--leaf);
  }
  .panel-tab {
    position: absolute; left: 416px; top: 388px;
  }
  .contact-list {
    list-style: none; position: absolute; left: 70px; top: 62px;
    font-family: "Raleway", sans-serif; font-weight: 600;
    font-variant: small-caps; font-size: 24px; letter-spacing: 2.5px;
    color: var(--ink-light); line-height: 1.2;
  }
  .contact-item { display: flex; align-items: flex-start; gap: 14px; margin-bottom: 20px; }
  .contact-item svg { flex: none; margin-top: 4px; }
  .divider {
    position: absolute; left: 70px; right: 60px; top: 336px;
    border-top: 3px dotted var(--ink-light);
  }
  .holder {
    position: absolute; right: 60px; top: 360px; text-align: right;
    font-family: "Oswald", sans-serif; color: var(--ink-light);
    text-transform: uppercase;
  }
  .holder-name { font-size: 62px; font-weight: 600; letter-spacing: 1px; line-height: 1.1; }
  .holder-title { font-size: 32px; font-weight: 500; letter-spacing: 1px; }
</style>
</head>
<body>
  <div class="card">
    <div class="brand-side">
      <span class="brand-dot"></span>
      <span class="brand-name">Lumo Bravo</span>
    </div>

    <svg class="panel-tab" width="30" height="40" viewBox="0 0 30 40" aria-hidden="true">
      <polygon points="24,0 30,0 30,40 24,40 0,20" fill="var(--leaf)"/>
    </svg>

    <div class="info-panel">
      <ul class="contact-list">
        <li class="contact-item">
          <svg width="20" height="20" viewBox="0 0 24 24" aria-hidden="true"><path d="M6 2l4 4-2 3c1 3 3 5 6 6l3-2 4 4-3 4C9 21 3 15 2 5z" fill="var(--icon-accent)"/></svg>
          <span>Tel: 714-382-5061</span>
        </li>
        <li class="contact-item">
          <svg width="20" height="20" viewBox="0 0 24 24" aria-hidden="true"><rect x="2" y="5" width="20" height="14" fill="none" stroke="#fff" stroke-width="2"/><path d="M2 5l10 8 10-8" fill="none" stroke="#fff" stroke-width="2"/></svg>
          <span>brenton@lumobravo.com</span>
        </li>
        <li class="contact-item">
          <svg width="20" height="20" viewBox="0 0 24 24" aria-hidden="true"><circle cx="12" cy="12" r="10" fill="none" stroke="#fff" stroke-width="2"/><ellipse cx="12" cy="12" rx="4" ry="10" fill="none" stroke="#fff" stroke-width="2"/><path d="M2 12h20" stroke="#fff" stroke-width="2"/></svg>
          <span>www.lumobravo.com</span>
        </li>
        <li class="contact-item">
          <svg width="20" height="20" viewBox="0 0 24 24" aria-hidden="true"><path d="M12 2L1 12h3v10h6v-6h4v6h6V12h3z" fill="#fff"/></svg>
          <span>38750 Harlow Ave, Suite 415<br>Irvine, CA 92604</span>
        </li>
      </ul>
      <div class="divider"></div>
      <div class="holder">
        <div class="holder-name">Brenton</div>
        <div class="holder-title">Sales Manager</div>
      </div>
    </div>
  </div>
</body>
</html>
```